Cosmetics Store Website

High end cosmetics/skincare store needs a new website. We are a locally owned company based in Idaho. We have an initial site map and some copy and we are looking for someone who can not only DESIGN but get a full website UP AND RUNNING! This will not be a shopping cart style site (we do not sell online) but rather an information site about our locations, our brands, our services, our mission, job opportunities etc. We would like to see a mock up of our home page and hear how you plan to code/set up the rest of our site. We would prefer to keep the company name confidential, but know that our logo is black and just a stylized lettering of our company name.
More details like company name, logo, pictures, etc can be given after we select a candidate.
Thank you!

```html
<!DOCTYPE html>
<html lang="en">
<head>
<meta charset="utf-8">
<title>Velora Skin Studio</title>
<link rel="stylesheet" href="https://fonts.googleapis.com/css2?family=Cinzel:wght@400;700&family=Noto+Serif:ital@0;1&family=Montserrat:wght@400;700&display=swap">
<style>
:root{
  --ink:#1c1c1c;
  --nav-bg:#f4f4f4;
  --soft-bg:#f7f7f7;
  --white:#ffffff;
  --accent:#e07f78;
  --line:#8a8a8a;
  --frame:#d6d6d6;
  --placeholder:#b4b4b4;
}
*{box-sizing:border-box;margin:0;padding:0}
html,body{width:753px;height:1200px;overflow:hidden;background:var(--white)}
body{position:relative;font-family:"Noto Serif",Georgia,serif;color:var(--ink)}
.abs{position:absolute}

/* header */
.site-header{left:0;top:0;width:753px;height:35px;background:var(--nav-bg)}
.brand{left:124px;top:8px;font-family:"Cinzel",serif;font-size:13px;font-weight:400;color:var(--ink);letter-spacing:.3px}
.main-nav{left:262px;top:13px;display:flex;gap:17px;font-family:"Cinzel",serif;font-size:8px;letter-spacing:.2px}

/* hero */
.hero{left:0;top:35px;width:753px;height:269px;background:var(--white)}
.hero-photo{left:350px;top:35px;width:403px;height:269px;
  background:linear-gradient(100deg,#ffffff 0%,#f9ece6 20%,#f2d6ca 55%,#ecc6b8 80%,#f1d2c8 100%)}
.hero-kicker{left:134px;top:137px;font-style:italic;font-size:17px}
.hero-title{left:134px;top:158px;font-family:"Cinzel",serif;font-size:29px;font-weight:400;letter-spacing:.3px}
.btn{background:var(--accent);color:var(--white);font-family:"Cinzel",serif;text-align:center}
.hero-btn{left:135px;top:205px;width:128px;height:34px;line-height:34px;font-size:14px}

/* features */
.feature-photo{top:336px;width:156px;height:107px;border:1px solid var(--frame)}
.feature-link{top:455px;width:102px;height:23px;border:1px solid var(--line);font-style:italic;font-size:8px;text-align:center;line-height:21px}
.feature-link svg{vertical-align:middle;margin-left:4px}

/* experts */
.experts{left:0;top:510px;width:753px;height:312px;background:var(--soft-bg)}
.section-title{left:0;width:753px;text-align:center;font-family:"Cinzel",serif;font-weight:400}
.experts-title{top:549px;font-size:21px}
.expert-photo{top:594px;width:124px;height:124px;border-radius:50%;border:3px solid var(--white)}
.expert-name{top:729px;width:160px;text-align:center;font-family:"Cinzel",serif;font-size:8px}
.expert-role{top:742px;width:160px;text-align:center;font-style:italic;font-size:7.5px}
.expert-social{top:757px;width:160px;display:flex;justify-content:center;gap:4px}

/* contact */
.contact{left:0;top:822px;width:753px;height:324px;
  background:linear-gradient(180deg,#5f5b5a 0%,#7a7472 40%,#8f8883 70%,#b0a9a2 100%)}
.contact-title{top:862px;font-size:23px;color:var(--white)}
.field{background:var(--white);border:1px solid #e2e2e2;font-family:"Montserrat",sans-serif;font-size:7px;font-weight:700;color:var(--placeholder);padding:9px 11px;letter-spacing:.3px}
.field-short{left:123px;width:246px;height:27px}
.field-message{left:384px;top:927px;width:245px;height:113px}
.send-btn{left:312px;top:1056px;width:128px;height:35px;line-height:35px;font-size:12px}

/* footer */
.site-footer{left:0;top:1146px;width:753px;height:54px;background:var(--white)}
.copyright{left:124px;top:1168px;font-family:"Montserrat",sans-serif;font-size:6.5px}
.footer-social{left:324px;top:1161px;display:flex;gap:3px}
</style>
</head>
<body>

<header class="abs site-header"></header>
<div class="abs brand">Velora Skin Studio</div>
<nav class="abs main-nav">
  <span>About</span><span>Locations</span><span>Our Brands</span><span>Our Services</span><span>Our Mission</span><span>Job Opportunities</span>
</nav>

<section class="abs hero"></section>
<div class="abs hero-photo" role="img" aria-label="Close-up portrait of a woman with closed eyes and pink lilies against her skin"></div>
<p class="abs hero-kicker">Get your flawless skin!</p>
<h1 class="abs hero-title">WITHIN FEW WEEKS</h1>
<div class="abs btn hero-btn">READ MORE</div>

<div class="abs feature-photo" style="left:124px;background:linear-gradient(135deg,#fbf6ec,#f3e0c8 60%,#f4d98a)" role="img" aria-label="Smiling woman holding lemon slices"></div>
<div class="abs feature-photo" style="left:299px;background:linear-gradient(135deg,#ffffff,#f0e4dc 60%,#e9dfd4)" role="img" aria-label="Woman resting beside skincare bottles and jars"></div>
<div class="abs feature-photo" style="left:474px;background:linear-gradient(135deg,#f8f2ea,#e9cfa6 55%,#d6b489)" role="img" aria-label="Woman receiving makeup and hair styling"></div>

<div class="abs feature-link" style="left:151px">Beauty Clinic<svg width="5" height="5" viewBox="0 0 5 5"><path d="M0 0L5 2.5 0 5z" fill="#1c1c1c"/></svg></div>
<div class="abs feature-link" style="left:326px">Cosmetic<svg width="5" height="5" viewBox="0 0 5 5"><path d="M0 0L5 2.5 0 5z" fill="#1c1c1c"/></svg></div>
<div class="abs feature-link" style="left:501px">Beauty Advice<svg width="5" height="5" viewBox="0 0 5 5"><path d="M0 0L5 2.5 0 5z" fill="#1c1c1c"/></svg></div>

<section class="abs experts"></section>
<h2 class="abs section-title experts-title">OUR EXPERTS</h2>

<div class="abs expert-photo" style="left:163px;background:linear-gradient(160deg,#eef4f8,#e8d6c0 50%,#f4f4f4)" role="img" aria-label="Portrait of the skin expert"></div>
<div class="abs expert-photo" style="left:314px;background:linear-gradient(160deg,#cfdde6,#7a5a48 50%,#f2f2f2)" role="img" aria-label="Portrait of the beauty consultant"></div>
<div class="abs expert-photo" style="left:464px;background:linear-gradient(160deg,#ffffff,#c9a48c 50%,#eef0f2)" role="img" aria-label="Portrait of the dermatology expert"></div>

<div class="abs expert-name" style="left:145px">Marisa Ellwood</div>
<div class="abs expert-role" style="left:145px">Skin Expert</div>
<div class="abs expert-social" style="left:145px">
  <svg width="23" height="23"><circle cx="11.5" cy="11.5" r="10.5" fill="none" stroke="#1c1c1c" stroke-width="1.6"/></svg>
  <svg width="23" height="23"><circle cx="11.5" cy="11.5" r="10.5" fill="none" stroke="#1c1c1c" stroke-width="1.6"/></svg>
  <svg width="23" height="23"><circle cx="11.5" cy="11.5" r="10.5" fill="none" stroke="#1c1c1c" stroke-width="1.6"/></svg>
</div>

<div class="abs expert-name" style="left:296px">Danica Ferreira</div>
<div class="abs expert-role" style="left:296px">Beauty Consultant</div>
<div class="abs expert-social" style="left:296px">
  <svg width="23" height="23"><circle cx="11.5" cy="11.5" r="10.5" fill="none" stroke="#1c1c1c" stroke-width="1.6"/></svg>
  <svg width="23" height="23"><circle cx="11.5" cy="11.5" r="10.5" fill="none" stroke="#1c1c1c" stroke-width="1.6"/></svg>
  <svg width="23" height="23"><circle cx="11.5" cy="11.5" r="10.5" fill="none" stroke="#1c1c1c" stroke-width="1.6"/></svg>
</div>

<div class="abs expert-name" style="left:446px">Tavin Rhodes</div>
<div class="abs expert-role" style="left:446px">Dermatology Expert</div>
<div class="abs expert-social" style="left:446px">
  <svg width="23" height="23"><circle cx="11.5" cy="11.5" r="10.5" fill="none" stroke="#1c1c1c" stroke-width="1.6"/></svg>
  <svg width="23" height="23"><circle cx="11.5" cy="11.5" r="10.5" fill="none" stroke="#1c1c1c" stroke-width="1.6"/></svg>
</div>

<section class="abs contact" role="img" aria-label="Treatment room interior with a white treatment bed and soft ceiling lights"></section>
<h2 class="abs section-title contact-title">CONTACT US</h2>
<div class="abs field field-short" style="top:927px">YOUR NAME *</div>
<div class="abs field field-short" style="top:969px">YOUR E-MAIL *</div>
<div class="abs field field-short" style="top:1013px">SUBJECT</div>
<div class="abs field field-message">YOUR MESSAGE *</div>
<div class="abs btn send-btn">SEND MESSAGE</div>

<footer class="abs site-footer"></footer>
<p class="abs copyright">© Copyright 2014 VeloraSkinStudio.com</p>
<div class="abs footer-social">
  <svg width="24" height="24"><circle cx="12" cy="12" r="11.5" fill="#1c1c1c"/></svg>
  <svg width="24" height="24"><circle cx="12" cy="12" r="11.5" fill="#1c1c1c"/></svg>
  <svg width="24" height="24"><circle cx="12" cy="12" r="11.5" fill="#1c1c1c"/></svg>
  <svg width="24" height="24"><circle cx="12" cy="12" r="11.5" fill="#1c1c1c"/></svg>
</div>

</body>
</html>
```